Copper Ridge Hitters Baseball Club (CRH)

Looking for a new web page for Middle School/High School focused baseball club that works with elite prospects. This site will introduce our program to the Northern Virginia area. We will need the ability to sell merchandise and 4+ Services

We would like to use a color theme that goes with our label attached.

We also already own the CRH-VX.com

Industry/Entity Type

Sports Baseball

Coding

Coded - Design and coding required

Number of Pages Required

5+ page

Colors
0054AA
0677BA
7BADD7
CADEEF
E8F1F8

Requirements
Must have
• Ability to upload photos. Page for player profiles/Program Description/Game stats and standings
Nice to have
• pinelakeprospectsball.com otterballclub.net quarrygritballclub.com

```html
<!DOCTYPE html>
<html lang="en">
<head>
<meta charset="utf-8">
<title>Copper Ridge Hitters Baseball Club</title>
<link rel="stylesheet" href="https://fonts.googleapis.com/css2?family=Saira+Semi+Condensed:wght@500;600;700&family=Mulish:wght@400;600;700&display=swap">
<style>
:root{
  --blue:#0054aa;
  --blue-mid:#0677ba;
  --blue-light:#7badd7;
  --blue-pale:#cadeef;
  --blue-mist:#e8f1f8;
  --navy:#0b2a52;
  --navy-deep:#0a2140;
  --ink:#16181d;
  --text:#3e434b;
  --white:#fff;
  --head:"Saira Semi Condensed","Arial Narrow",sans-serif;
  --body:"Mulish",sans-serif;
}
*{box-sizing:border-box;margin:0;padding:0}
html,body{width:1200px;height:3578px;overflow:hidden}
body{position:relative;background:var(--white);font-family:var(--body);color:var(--text)}
.abs{position:absolute}
a{color:inherit;text-decoration:none}

/* header */
.site-header{left:0;top:0;width:1200px;height:77px;background:var(--white);z-index:3}
.brand{left:129px;top:8px;display:flex;align-items:center;gap:10px}
.brand-dot{width:54px;height:54px;border-radius:50%;background:var(--blue)}
.brand-name{font-family:var(--head);font-weight:700;font-size:34px;color:var(--navy)}
.top-contact{right:129px;top:10px;font-size:12px;color:var(--blue);display:flex;gap:16px;align-items:center}
.top-contact span{display:flex;align-items:center;gap:4px}
.main-nav{left:383px;top:51px;display:flex;width:688px;justify-content:space-between;font-family:var(--head);font-weight:600;font-size:12px;color:var(--ink);white-space:nowrap}
.main-nav .active{color:var(--blue)}

/* hero */
.hero{left:0;top:77px;width:1200px;height:490px;overflow:hidden;background:linear-gradient(90deg,#3b3f2c 0%,#6b6a52 30%,#4e5a3a 60%,#2f3a26 100%)}
.hero-figure{left:120px;top:0;width:560px;height:490px;background:radial-gradient(ellipse at 50% 55%,#c8c2b8 0%,#8b3a3a 35%,rgba(60,60,50,0) 70%)}
.hero-copy{left:736px;top:128px;border-left:2px solid var(--blue-mid);padding-left:18px;color:var(--white)}
.hero-kicker{font-family:var(--head);font-weight:500;font-size:18px;letter-spacing:.5px}
.hero-title{font-family:var(--head);font-weight:700;font-size:46px;line-height:48px;margin-top:6px;white-space:nowrap}
.hero-lead{font-size:14px;line-height:19px;margin-top:16px;width:330px}
.btn{display:inline-block;background:var(--blue);color:var(--white);font-family:var(--body);font-weight:700;font-size:11px;text-transform:uppercase;text-align:center;letter-spacing:.3px;white-space:nowrap}
.hero .btn{margin-top:18px;width:142px;height:39px;line-height:39px}
.hero-dots{left:1025px;top:440px}

/* news */
.section-title{font-family:var(--head);font-weight:700;font-size:32px;color:var(--ink);text-transform:uppercase;left:129px;white-space:nowrap}
.section-title em{font-style:normal;color:var(--blue)}
.card-row{left:129px;width:941px;display:flex;justify-content:space-between}
.news-card{width:300px}
.photo{display:block;width:100%}
.news-card .photo{height:201px}
.card-title{font-family:var(--head);font-weight:700;font-size:15px;color:var(--ink);text-transform:uppercase;margin-top:16px;white-space:nowrap}
.card-text{font-size:12.5px;line-height:18px;margin-top:12px}
.news-card .btn{margin-top:18px;width:101px;height:35px;line-height:35px}
.slider-arrow{width:34px;height:34px;border:1px solid #555;background:var(--white);display:flex;align-items:center;justify-content:center}
.divider{left:129px;top:1088px;width:941px;height:1px;background:#e2e4e8}

/* about */
.about{left:0;top:1642px;width:1200px;height:485px;background:linear-gradient(120deg,#0e4c8c 0%,#0b3a72 35%,#0a2d5a 70%)}
.about-photo{left:0;top:0;width:1200px;height:485px;clip-path:polygon(549px 0,1200px 0,1200px 485px,764px 485px);background:linear-gradient(135deg,#b57a4f 0%,#8a5533 40%,#d9c9a0 70%,#6e4a30 100%)}
.about-stripe{left:0;top:0;width:1200px;height:485px;clip-path:polygon(540px 0,549px 0,764px 485px,755px 485px);background:var(--white)}
.about-copy{left:129px;top:55px;color:var(--white);width:440px}
.about-kicker{font-family:var(--head);font-weight:500;font-size:19px}
.about-title{font-family:var(--head);font-weight:700;font-size:31px;line-height:37px;margin-top:2px;white-space:nowrap}
.about-text{font-size:14px;line-height:21.5px;margin-top:24px}
.about .btn{margin-top:36px;width:101px;height:36px;line-height:36px}

/* merchandise */
.merch-card{width:221px;text-align:center}
.merch-photo{position:relative;height:225px;background:var(--blue-mist)}
.shirt{position:absolute;left:40px;top:18px;width:141px;height:170px;border-radius:18px 18px 6px 6px}
.merch-tag{position:absolute;left:50%;bottom:-15px;transform:translateX(-50%);width:130px;height:30px;line-height:30px;background:var(--blue);color:var(--white);font-family:var(--head);font-weight:600;font-size:12px;clip-path:polygon(12px 0,100% 0,calc(100% - 12px) 100%,0 100%)}
.merch-card .card-title{margin-top:28px}
.merch-card .card-text{font-family:Arial,sans-serif;font-size:12.5px;margin-top:10px}

/* services */
.services{left:0;top:2660px;width:1200px;height:540px;clip-path:polygon(0 35px,1200px 0,1200px 540px,0 540px);background:radial-gradient(ellipse at 20% 40%,#1d4a5a 0%,#10324a 40%,#0a223d 80%)}
.services-title{left:0;width:1200px;top:2717px;text-align:center;font-family:var(--head);font-weight:700;font-size:31px;color:var(--white)}
.service-card{width:221px;color:var(--white)}
.service-card .photo{height:186px}
.service-card .card-title{color:var(--white);font-size:14.5px;margin-top:16px}
.service-card .card-text{color:#c9d3df;margin-top:12px}
.service-card .btn{margin-top:24px;width:102px;height:36px;line-height:36px}

/* footer */
.site-footer{left:0;top:3160px;width:1200px;height:418px;background:var(--navy-deep);clip-path:polygon(0 0,1200px 28px,1200px 418px,0 418px);color:var(--white)}
.foot-col{top:82px}
.foot-head{font-family:var(--head);font-weight:600;font-size:15px;text-transform:uppercase;margin-bottom:14px}
.foot-list{list-style:none;font-size:12px;line-height:26px;white-space:nowrap}
.foot-rule{top:78px;width:1px;height:190px;background:#24406a}
.news-input{width:198px;height:31px;background:var(--white);font-size:9px;color:#555;padding:10px 11px;margin-bottom:4px}
.news-btn{width:198px;height:31px;line-height:31px;text-align:center;background:var(--blue);font-size:11px;font-weight:700}
.social{left:561px;top:305px;display:flex;gap:8px}
.social span{width:18px;height:18px;background:var(--blue)}
.copyright{left:0;width:1200px;top:337px;text-align:center;font-size:10.5px;color:#8a9ab0}
.copyright b{color:var(--white);font-weight:400}
</style>
</head>
<body>

<header class="site-header abs">
  <a class="brand abs" href="#"><span class="brand-dot"></span><span class="brand-name">CRH</span></a>
  <div class="top-contact abs">
    <span><svg width="10" height="10" viewBox="0 0 24 24"><path fill="#0b2a52" d="M6.6 10.8a15 15 0 0 0 6.6 6.6l2.2-2.2a1 1 0 0 1 1-.25 11.4 11.4 0 0 0 3.6.6 1 1 0 0 1 1 1V20a1 1 0 0 1-1 1A17 17 0 0 1 3 4a1 1 0 0 1 1-1h3.5a1 1 0 0 1 1 1c0 1.25.2 2.45.6 3.6a1 1 0 0 1-.25 1z"/></svg>+2 (555) 240 7300</span>
    <span><svg width="11" height="9" viewBox="0 0 24 18"><rect width="24" height="18" fill="#0b2a52"/><path d="M0 0l12 9 12-9" stroke="#fff" stroke-width="2" fill="none"/></svg>coach.hale@crh-vx.com</span>
  </div>
  <nav class="main-nav abs">
    <a class="active" href="#">HOME</a><a href="#">ABOUT US</a><a href="#">MIDDLE SCHOOL</a><a href="#">HIGH SCHOOL</a><a href="#">SERVICES</a><a href="#">MERCHANDISE</a><a href="#">CONTACT US</a>
  </nav>
</header>

<section class="hero abs">
  <div class="hero-figure abs" role="img" aria-label="Catcher in red gear crouched behind home plate with umpire behind"></div>
  <div class="hero-copy abs">
    <div class="hero-kicker">PLAYS IN</div>
    <h1 class="hero-title">RCTBL<br>ON WEEKENDS</h1>
    <p class="hero-lead">Participation in SwingGrid BP Leagues is included for any CRHBC Team Member.</p>
    <a class="btn" href="#">About our team</a>
  </div>
  <svg class="hero-dots abs" width="46" height="15" viewBox="0 0 46 15"><polygon points="5,0 13,0 8,15 0,15" fill="var(--blue-mid)"/><polygon points="20,0 28,0 23,15 15,15" fill="#fff"/><polygon points="35,0 43,0 38,15 30,15" fill="#fff"/></svg>
</section>

<h2 class="section-title abs" style="top:636px"><em>Middle School</em> News</h2>
<div class="slider-arrow abs" style="left:49px;top:785px"><svg width="10" height="14" viewBox="0 0 10 14"><path d="M8 1L2 7l6 6" stroke="#222" stroke-width="1.6" fill="none"/></svg></div>
<div class="slider-arrow abs" style="left:1118px;top:785px"><svg width="10" height="14" viewBox="0 0 10 14"><path d="M2 1l6 6-6 6" stroke="#222" stroke-width="1.6" fill="none"/></svg></div>
<div class="card-row abs" style="top:700px">
  <article class="news-card"><div class="photo" role="img" aria-label="Youth batter swinging with catcher and umpire behind" style="background:linear-gradient(180deg,#5e6c7c 0%,#43623b 45%,#a2603f 100%)"></div><h3 class="card-title">Sed ut perspiciatis unde omnis 2021</h3><p class="card-text">Nor again is there anyone who loves or pursues or desires to obtain pain of itself</p><a class="btn" href="#">Read more</a></article>
  <article class="news-card"><div class="photo" role="img" aria-label="Close-up of a batter in helmet swinging at night" style="background:linear-gradient(160deg,#4b4a2e 0%,#2a2617 50%,#6a2c3c 100%)"></div><h3 class="card-title">Sed ut perspiciatis unde omnis 2021</h3><p class="card-text">Nor again is there anyone who loves or pursues or desires to obtain pain of itself</p><a class="btn" href="#">Read more</a></article>
  <article class="news-card"><div class="photo" role="img" aria-label="Young hitter in blue uniform swinging by a fence" style="background:linear-gradient(180deg,#8a8a7a 0%,#6b7760 50%,#b58a66 100%)"></div><h3 class="card-title">Sed ut perspiciatis unde omnis 2021</h3><p class="card-text">Nor again is there anyone who loves or pursues or desires to obtain pain of itself</p><a class="btn" href="#">Read more</a></article>
</div>

<div class="divider abs"></div>

<h2 class="section-title abs" style="top:1156px"><em>High School</em> News</h2>
<div class="slider-arrow abs" style="left:49px;top:1306px"><svg width="10" height="14" viewBox="0 0 10 14"><path d="M8 1L2 7l6 6" stroke="#222" stroke-width="1.6" fill="none"/></svg></div>
<div class="slider-arrow abs" style="left:1118px;top:1306px"><svg width="10" height="14" viewBox="0 0 10 14"><path d="M2 1l6 6-6 6" stroke="#222" stroke-width="1.6" fill="none"/></svg></div>
<div class="card-row abs" style="top:1221px">
  <article class="news-card"><div class="photo" role="img" aria-label="Batter in red jersey at the plate with teammates behind" style="background:linear-gradient(180deg,#5a6a4c 0%,#6f7b57 50%,#a88062 100%)"></div><h3 class="card-title">Sed ut perspiciatis unde omnis 2021</h3><p class="card-text">Nor again is there anyone who loves or pursues or desires to obtain pain of itself</p><a class="btn" href="#">Read more</a></article>
  <article class="news-card"><div class="photo" role="img" aria-label="Stadium view of a batter swinging before a crowd" style="background:linear-gradient(180deg,#2c3a56 0%,#3e5a78 40%,#4f7b3c 70%,#8a6a4a 100%)"></div><h3 class="card-title">Sed ut perspiciatis unde omnis 2021</h3><p class="card-text">Nor again is there anyone who loves or pursues or desires to obtain pain of itself</p><a class="btn" href="#">Read more</a></article>
  <article class="news-card"><div class="photo" role="img" aria-label="Young pitcher mid-throw on a green background" style="background:linear-gradient(160deg,#5e8a3a 0%,#8cad4e 50%,#d8d2c4 100%)"></div><h3 class="card-title">Sed ut perspiciatis unde omnis 2021</h3><p class="card-text">Nor again is there anyone who loves or pursues or desires to obtain pain of itself</p><a class="btn" href="#">Read more</a></article>
</div>

<section class="about abs">
  <div class="about-photo abs" role="img" aria-label="Catcher with mitt raised on a clay infield"></div>
  <div class="about-stripe abs"></div>
  <div class="about-copy abs">
    <div class="about-kicker">ABOUT THE</div>
    <h2 class="about-title">COPPER RIDGE HITTERS<br>BASEBALL CLUB</h2>
    <p class="about-text">The CRHBC is the first team in the DMV that will be selecting players from it's tryout pool that show promise in OVERALL athletic ability and PLATE AGRESSIVENESS. Our tryouts will consist of 1) a comprehensive assessment of speed, power, balance, mobility and baseball SPECIFIC movement (the Copper Ridge Combine), and 2) a data-driven assessment of plate discipline, aggressiveness, and launch metrics; the cutting edge of baseball testing ability.</p>
    <a class="btn" href="#">Read more</a>
  </div>
</section>

<h2 class="section-title abs" style="top:2194px"><em>Merchandise</em></h2>
<div class="card-row abs" style="top:2259px">
  <article class="merch-card"><div class="merch-photo"><div class="shirt" role="img" aria-label="Navy and orange team jersey" style="background:linear-gradient(90deg,#2a2f6a 60%,#e08a2a 60%)"></div><span class="merch-tag">CRH-VX.COM</span></div><h3 class="card-title">Bonorum et malorum</h3><p class="card-text">Quis nostrum exercitationem ullam corporis</p></article>
  <article class="merch-card"><div class="merch-photo"><div class="shirt" role="img" aria-label="Red and navy team jersey" style="background:linear-gradient(90deg,#1d2455 20%,#c0152a 75%)"></div><span class="merch-tag">CRH-VX.COM</span></div><h3 class="card-title">Bonorum et malorum</h3><p class="card-text">Quis nostrum exercitationem ullam corporis</p></article>
  <article class="merch-card"><div class="merch-photo"><div class="shirt" role="img" aria-label="Dark green team jersey with red sleeves" style="background:linear-gradient(90deg,#d8404e 12%,#2f4a48 12%,#2f4a48 88%,#d8404e 88%)"></div><span class="merch-tag">CRH-VX.COM</span></div><h3 class="card-title">Bonorum et malorum</h3><p class="card-text">Quis nostrum exercitationem ullam corporis</p></article>
  <article class="merch-card"><div class="merch-photo"><div class="shirt" role="img" aria-label="Purple and gold team jersey" style="background:linear-gradient(120deg,#4a1f6a 40%,#e0a91a 60%)"></div><span class="merch-tag">CRH-VX.COM</span></div><h3 class="card-title">Bonorum et malorum</h3><p class="card-text">Quis nostrum exercitationem ullam corporis</p></article>
</div>

<section class="services abs" role="img" aria-label="Dark background of a baseball close-up"></section>
<h2 class="services-title abs">OUR SERVICES</h2>
<div class="card-row abs" style="top:2775px">
  <article class="service-card"><div class="photo" role="img" aria-label="Pitcher on the mound in a large stadium" style="background:linear-gradient(180deg,#6b8ab0 0%,#8a6a5a 35%,#3f7a3a 60%,#4e7a3c 100%)"></div><h3 class="card-title">Similique sunt in culpa qui</h3><p class="card-text">Quis nostrum exercitationem ullam corporis there anyone who loves or pursues or desires to obtain pain of itself...</p><a class="btn" href="#">Read more</a></article>
  <article class="service-card"><div class="photo" role="img" aria-label="Pitcher in pinstripes delivering a pitch" style="background:linear-gradient(160deg,#6f7a74 0%,#a8aeb0 50%,#7a5a4e 100%)"></div><h3 class="card-title">Similique sunt in culpa qui</h3><p class="card-text">Quis nostrum exercitationem ullam corporis there anyone who loves or pursues or desires to obtain pain of itself...</p><a class="btn" href="#">Read more</a></article>
  <article class="service-card"><div class="photo" role="img" aria-label="Runner sliding into base as a fielder tags" style="background:linear-gradient(180deg,#4a7a3a 0%,#6a8a4a 40%,#9a6a4a 100%)"></div><h3 class="card-title">Similique sunt in culpa qui</h3><p class="card-text">Quis nostrum exercitationem ullam corporis there anyone who loves or pursues or desires to obtain pain of itself...</p><a class="btn" href="#">Read more</a></article>
  <article class="service-card"><div class="photo" role="img" aria-label="Play at home plate at dusk" style="background:linear-gradient(180deg,#8a8a8e 0%,#5a7a4a 50%,#4a6a3a 100%)"></div><h3 class="card-title">Similique sunt in culpa qui</h3><p class="card-text">Quis nostrum exercitationem ullam corporis there anyone who loves or pursues or desires to obtain pain of itself...</p><a class="btn" href="#">Read more</a></article>
</div>

<footer class="site-footer abs">
  <div class="foot-col abs" style="left:129px"><h4 class="foot-head">Quick Links</h4><ul class="foot-list"><li>Home</li><li>About Us</li><li>Middle School</li><li>High School</li><li>Services</li><li>Merchandise</li><li>Contact Us</li></ul></div>
  <div class="foot-rule abs" style="left:251px"></div>
  <div class="foot-col abs" style="left:289px"><h4 class="foot-head">Contacts</h4><p style="font-size:12px;line-height:16px">4180 Harbor Mill Rd Suite B<br>Fairlane, VX 20917</p><p style="font-size:12px;margin-top:20px">+2 (555) 240 7300</p><p style="font-size:12px;margin-top:20px">coach.hale@crh-vx.com</p></div>
  <div class="foot-rule abs" style="left:507px"></div>
  <div class="foot-col abs" style="left:543px"><h4 class="foot-head">Newsletter</h4><div class="news-input">Name:</div><div class="news-input">Email:</div><div class="news-btn">SIGNUP</div></div>
  <div class="foot-rule abs" style="left:768px"></div>
  <div class="foot-col abs" style="left:796px"><h4 class="foot-head">Ballplayers</h4><ul class="foot-list"><li>Driven and motivated to stand out!!!</li><li>High motor</li><li>Aggressive offensive mindset</li><li>All positions - any experience level</li><li>Multi-sport athletes strongly encouraged to tryout</li></ul></div>
  <div class="social abs"><span></span><span></span><span></span></div>
  <p class="copyright abs">Copyright © 2021 <b>Copper Ridge Hitters Baseball</b>. All Rights Reserved.</p>
</footer>

</body>
</html>
```